Visitenkarten-Design für Familienunternehmen (Apotheke)
Zielgruppe
Wir sind ein Familienunternehmen und betreiben 4 Apotheken (alle eigene Namen: Lindenhof-Apotheke; Kessel-Apotheke; VeroNova-Apotheke und VeroNova-Apotheke)
Wir beginnen, diese alle unter Sperling-Apotheken zusammenzufassen. www.sperling-apotheken.de (die VeroNova-Apotheke eröffnet erst am 1.1.18 neu, daher noch nicht online)
Konkret möchten wir für die Mitarbeiter der VeroNova-Apotheke Visitenkarten mit Porträt für Kunden erstellen.
Aktuell sind wir ca. 10 Mitarbeiter in dieser Apotheke. Ggf. möchten wir mittelfristig alle Mitarbeiter aller Apotheken (ca. 50-60) mit Visitenkarten ausstatten.
Aufgabenstellung
Wir haben vor Jahren selbst laienhaft eine Visitenkarte erstellt
Ich habe gegoogelt und andere Beispiele mit Porträt gefunden.
Wir suchen eine Visitenkarte, die sowohl das Logo VeroNova-Apotheke inkl. Adresse, Telefonnummer etc. hat (kann auch optisch verschoben werden - oben Logo - unten Adresse o.ä) , den Namen des Mitarbeitern und Beruf (Apothekerin o.ä.) und 2-3 Schlagwörter/Schlagsätze zu der Qualifikation des Mitarbeiters.
(die VeroNova-Apotheke hat eine Spezialzertifizierung 'Wiegensichere Offizin' und darf daher auch das Logo Wiegensichere Offizin nutzen. Eventuell gibt es die Möglichkeit dieses auch - nicht konkurrierend - neben dem Hauptlogo VeroNova-Apotheke unterzubringen)
unten gerne 'Sperling-Apotheken' o.ä. als Dachmarke
Mutter-Kind-Expertin (Zertifizierung Wiegensichere Offizin)
Fachberaterin für Darmgesundheit
!! Seriös, weniger verspielt. Druckbar für Druckwerk24, wir nehmen gerne Tipps zu Papier und Stärke an!
Ziel: Klares Design, wo einfach der Kopf des Mitarbeiters gewechselt werden kann und die Qualifikation, um für alle Mitarbeiter gleiche CI zu erstellen

```html
<!DOCTYPE html>
<html lang="de">
<head>
<meta charset="utf-8">
<title>Visitenkarte – VeroNova-Apotheke</title>
<link rel="stylesheet" href="https://fonts.googleapis.com/css2?family=Open+Sans:ital,wght@0,300;0,400;0,600;0,700;1,600&display=swap">
<style>
  :root {
    --ink: #111111;
    --contact: #4a4a4a;
    --accent: #e30613;
    --muted: #9a9a9a;
    --paper: #ffffff;
    --portrait-dark: #2b2f45;
    --portrait-mid: #5a3f35;
    --portrait-light: #e9b8a8;
  }
  * { margin: 0; padding: 0; box-sizing: border-box; }
  html, body {
    width: 1200px; height: 777px; overflow: hidden; background: var(--paper);
  }
  .card {
    position: relative; width: 1200px; height: 777px;
    background: var(--paper); overflow: hidden;
    font-family: "Open Sans", Arial, sans-serif;
  }
  .corner-accent { position: absolute; inset: 0; z-index: 0; }
  .brand {
    position: absolute; left: 52px; top: 52px;
    display: flex; align-items: flex-start; gap: 12px;
  }
  .brand-name {
    font-weight: 700; font-size: 50px; line-height: 0.98;
    color: var(--ink); letter-spacing: -1.5px;
  }
  .brand-dot {
    width: 26px; height: 26px; border-radius: 50%;
    background: var(--accent); margin-top: 4px;
  }
  .contact {
    position: absolute; left: 506px; top: 38px;
    font-size: 22px; line-height: 32px; color: var(--contact);
    font-weight: 600; letter-spacing: -0.4px;
  }
  .contact .web-main { color: var(--accent); margin-top: 3px; }
  .employee {
    position: absolute; left: 53px; top: 362px; width: 600px;
  }
  .employee-name {
    font-size: 48px; font-weight: 700; color: var(--ink);
    line-height: 58px; letter-spacing: 0.2px;
  }
  .employee-branch {
    font-size: 33px; font-weight: 600; font-style: italic;
    color: var(--accent); line-height: 44px;
  }
  .employee-role {
    font-size: 30px; font-weight: 400; color: var(--muted);
    line-height: 46px;
  }
  .qualifications {
    list-style: none; margin-top: 6px;
  }
  .qualifications li {
    font-size: 24px; font-weight: 400; color: var(--muted);
    line-height: 36px; display: flex; align-items: center; gap: 12px;
  }
  .qualifications li::before {
    content: ""; width: 9px; height: 9px; background: var(--accent); flex: none;
  }
  .umbrella-brand {
    position: absolute; left: 53px; bottom: 40px;
    font-size: 24px; font-weight: 600; color: var(--contact);
    letter-spacing: 0.2px;
  }
  .portrait {
    position: absolute; left: 676px; top: 268px;
    width: 466px; height: 464px; z-index: 1;
    border-radius: 46% 46% 6px 6px / 38% 38% 6px 6px;
    background: linear-gradient(180deg, var(--portrait-mid) 0%, var(--portrait-light) 45%, var(--portrait-dark) 78%, var(--portrait-dark) 100%);
  }
</style>
</head>
<body>
  <div class="card">
    <svg class="corner-accent" width="1200" height="777" viewBox="0 0 1200 777" aria-hidden="true">
      <polygon points="962,777 1200,538 1200,777" fill="var(--accent)"/>
      <polygon points="1016,753 1177,592 1177,753" fill="var(--paper)"/>
    </svg>

    <div class="brand">
      <div class="brand-name">VeroNova-<br>Apotheke</div>
      <div class="brand-dot"></div>
    </div>

    <div class="contact">
      <div>Glockengasse 7 - 93410 Fernbach - Tel.: 09472 / 38 50 140</div>
      <div>Fax: 38 50 141 - veronova@sperling-apotheken.de</div>
      <div class="web-main">www.sperling-apotheken.de</div>
      <div class="web-cert">www.wiegensichere-offizin.de</div>
    </div>

    <div class="employee">
      <div class="employee-name">Hanna Vellmer</div>
      <div class="employee-branch">VeroNova-Apotheke</div>
      <div class="employee-role">Apothekerin</div>
      <ul class="qualifications">
        <li>Mutter-Kind-Expertin</li>
        <li>Zertifizierung Wiegensichere Offizin</li>
        <li>Fachberaterin für Darmgesundheit</li>
      </ul>
    </div>

    <div class="umbrella-brand">Ein Haus der Sperling-Apotheken</div>

    <div class="portrait" role="img" aria-label="Porträtfoto der Mitarbeiterin"></div>
  </div>
</body>
</html>
```